Harbourline Refrigeration business card design

We would like a new design for our business card as we have a new logo.
We need generic business card to give our customers with our office details - with the option of making it individualized for each manager

Target Market(s)

Companies and homeowners

Industry/Entity Type

Air Conditioning

Contact Information for Business Card

We are not sure if we want single or double sided it will depend on the design we choose

Colors
33a6d7
0255a3

Requirements
Must have
• Logo
• phone: (08) 8721 5940
• email: harbourserve@tealnet.example
• website: www.harbourlinerefrigeration.example
• AU61420
• BLD472913
Nice to have
• Address - Shed 5/284 Tallis Rd, Whyalla Norrie SA 5608

```html
<!DOCTYPE html>
<html lang="en">
<head>
<meta charset="utf-8">
<title>Harbourline Refrigeration – Business Card</title>
<link href="https://fonts.googleapis.com/css2?family=Montserrat:wght@500;600;700&family=Arimo:wght@400&display=swap" rel="stylesheet">
<style>
  :root {
    --stage: #2b2b2d;
    --navy: #1e3f7f;
    --brand-blue: #0255a3;
    --sky: #33a6d7;
    --card-blue: #1f4b95;
    --card-blue-deep: #193f80;
    --paper: #ffffff;
    --paper-tint: #eceaf5;
    --rule: #3b2f6b;
    --light-text: #e8ebf2;
  }
  * { box-sizing: border-box; margin: 0; padding: 0; }
  html, body { width: 1200px; height: 905px; overflow: hidden; }
  body {
    background: var(--stage);
    position: relative;
    font-family: "Arimo", Arial, sans-serif;
  }
  .card {
    position: absolute;
    width: 560px;
    height: 340px;
    border-radius: 22px;
    overflow: hidden;
  }
  /* Back side */
  .card-back {
    left: 50px; top: 70px;
    background: linear-gradient(135deg, var(--card-blue) 0%, var(--card-blue-deep) 100%);
  }
  .card-back .pattern-field {
    position: absolute; inset: 0;
    background: linear-gradient(135deg, rgba(255,255,255,0.05), rgba(255,255,255,0.02));
  }
  .card-back .brand {
    position: absolute; left: 0; right: 0; top: 128px;
    text-align: center;
    font-family: "Montserrat", Arial, sans-serif;
    font-weight: 600;
    font-size: 26px;
    color: var(--light-text);
  }
  .card-back .brand-dot {
    display: block;
    width: 34px; height: 34px;
    margin: 0 auto 14px;
    border-radius: 50%;
    background: var(--light-text);
  }
  .card-back .web {
    position: absolute; right: 40px; bottom: 36px;
    font-family: "Montserrat", Arial, sans-serif;
    font-weight: 600;
    font-size: 10px;
    letter-spacing: 0.8px;
    color: var(--light-text);
    text-transform: uppercase;
  }
  /* Front side */
  .card-front {
    left: 590px; top: 495px;
    background: var(--paper);
  }
  .card-front .pattern-field {
    position: absolute; left: 0; top: 0; bottom: 0; width: 260px;
    background: linear-gradient(90deg, var(--paper-tint) 0%, rgba(236,234,245,0) 100%);
  }
  .card-front .brand {
    position: absolute; right: 34px; top: 52px;
    display: flex; align-items: center; gap: 10px;
    font-family: "Montserrat", Arial, sans-serif;
    font-weight: 600;
    font-size: 22px;
    color: var(--navy);
  }
  .card-front .brand-dot {
    width: 24px; height: 24px; border-radius: 50%;
    background: var(--sky);
  }
  .card-front .rule {
    position: absolute; left: 236px; right: 34px; top: 168px;
    height: 1.5px; background: var(--rule);
  }
  .card-front .licences {
    position: absolute; right: 34px; top: 108px;
    text-align: right;
    font-size: 13px; line-height: 17px;
    color: var(--navy);
  }
  .card-front .person {
    position: absolute; left: 34px; top: 150px;
  }
  .person .name {
    font-family: "Montserrat", Arial, sans-serif;
    font-weight: 700; font-size: 21px;
    letter-spacing: 0.5px;
    color: var(--navy);
    text-transform: uppercase;
  }
  .person .role {
    font-family: "Montserrat", Arial, sans-serif;
    font-weight: 500; font-size: 14px;
    color: var(--sky);
    margin-top: 2px;
  }
  .contacts {
    position: absolute; left: 34px; top: 222px;
    list-style: none;
    font-size: 14px; color: var(--navy);
  }
  .contacts li {
    display: flex; align-items: center; gap: 10px;
    height: 24px;
  }
  .contacts svg { width: 14px; height: 14px; flex: none; }
</style>
</head>
<body>

  <section class="card card-back" aria-label="Business card back">
    <div class="pattern-field" role="img" aria-label="Faint repeating snowflake pattern"></div>
    <div class="brand"><span class="brand-dot"></span>Harbourline Refrigeration</div>
    <div class="web">www.harbourlinerefrigeration.example</div>
  </section>

  <section class="card card-front" aria-label="Business card front">
    <div class="pattern-field" role="img" aria-label="Faint repeating snowflake pattern"></div>
    <div class="brand"><span class="brand-dot"></span>Harbourline Refrigeration</div>
    <div class="licences">AU61420<br>BLD472913</div>
    <div class="rule"></div>
    <div class="person">
      <div class="name">Daniel Hart</div>
      <div class="role">Managing Director</div>
    </div>
    <ul class="contacts">
      <li>
        <svg viewBox="0 0 16 16" aria-hidden="true"><path fill="#33a6d7" d="M3.6 1.5l2.3 2.6-1.2 1.7c.9 2 2.6 3.7 4.6 4.6l1.7-1.2 2.6 2.3-1.5 2.5C6.9 13.7 2.3 9.1 1.1 3z"/></svg>
        (08) 8721 5940
      </li>
      <li>
        <svg viewBox="0 0 16 16" aria-hidden="true"><rect x="1" y="3" width="14" height="10" fill="#33a6d7"/><path d="M1 3l7 6 7-6" fill="none" stroke="#fff" stroke-width="1.3"/></svg>
        harbourserve@tealnet.example
      </li>
      <li>
        <svg viewBox="0 0 16 16" aria-hidden="true"><g fill="none" stroke="#33a6d7" stroke-width="1.4"><circle cx="8" cy="8" r="6.5"/><ellipse cx="8" cy="8" rx="3" ry="6.5"/><path d="M1.5 8h13M2.5 5h11M2.5 11h11"/></g></svg>
        www.harbourlinerefrigeration.example
      </li>
    </ul>
  </section>

</body>
</html>
```